Marwick Jewelers New Website Design

This project is to provide a new design for an existing website. The existing website is marwickjewelers dot com . I have created a overview document that outlines all the details for the project. I do not need the design to be converted into HTML. I have a team for that already so please don't ask. I have a lot of images .. too many to upload here so they are on my dev server located at pinefoxstudio com slash marwick slash assets

Number of Pages Required

1 page

```html
<!DOCTYPE html>
<html lang="en">
<head>
<meta charset="utf-8">
<title>Marwick Jewelers</title>
<link href="https://fonts.googleapis.com/css2?family=Great+Vibes&family=EB+Garamond:wght@400;500;600&family=Montserrat:wght@400;500;600&display=swap" rel="stylesheet">
<style>
:root{
  --teal:#3d7b86;
  --teal-dark:#2f6470;
  --teal-pale:#e3f0f2;
  --teal-mist:#eef6f7;
  --ink:#2b2b2b;
  --muted:#6b6b6b;
  --white:#ffffff;
  --black:#0d0d0d;
  --hero-dark:#1f2329;
  --photo-light:#f4f4f2;
  --photo-shade:#e6e6e3;
}
*{margin:0;padding:0;box-sizing:border-box}
html,body{width:1200px;height:4376px;overflow:hidden}
body{position:relative;background:var(--white);font-family:"EB Garamond",Georgia,serif;color:var(--ink)}
.abs{position:absolute}
.script{font-family:"Great Vibes",cursive;font-weight:400}

/* header */
.site-header{left:0;top:0;width:1200px;height:72px;background:var(--white)}
.brand{left:40px;top:6px;display:flex;align-items:center;gap:10px}
.brand-dot{width:14px;height:14px;border-radius:50%;background:var(--teal)}
.brand-name{font-family:"EB Garamond",serif;font-size:30px;font-weight:500;color:var(--teal);white-space:nowrap}
.util-bar{left:560px;top:0;width:640px;height:22px;background:var(--teal);display:flex;align-items:center;gap:22px;padding-left:40px;clip-path:polygon(4% 0,100% 0,100% 100%,0 100%)}
.util-bar span{font-family:"Montserrat",sans-serif;font-size:9px;letter-spacing:.8px;color:var(--white);white-space:nowrap}
.main-nav{left:0;top:46px;width:1200px;height:26px;background:var(--teal-mist);display:flex;align-items:center;padding-left:110px;gap:26px}
.main-nav span{font-family:"Montserrat",sans-serif;font-size:10px;font-weight:500;letter-spacing:1px;color:var(--teal-dark);white-space:nowrap}
.main-nav .on{border-bottom:2px solid var(--teal)}
.search{left:1010px;top:49px;width:90px;height:20px;border:1px solid var(--teal);border-radius:10px;font-family:"Montserrat",sans-serif;font-size:9px;color:var(--teal);display:flex;align-items:center;padding-left:12px;background:var(--white)}

/* hero */
.hero{left:0;top:72px;width:1200px;height:650px;background:radial-gradient(ellipse at 60% 70%,#8a8f99 0%,#474c55 30%,var(--hero-dark) 70%);clip-path:polygon(0 0,100% 0,100% 88%,0 100%)}
.hero-title{left:0;top:320px;width:1200px;text-align:center;font-size:72px;line-height:80px;color:var(--white)}
.hero-sub{left:0;top:402px;width:1200px;text-align:center;font-size:32px;line-height:40px;color:var(--white)}
.arrow-tab{width:26px;height:40px;background:var(--teal);display:flex;align-items:center;justify-content:center}
.btn{height:36px;border-radius:18px;background:var(--teal);display:flex;align-items:center;gap:18px;padding:0 6px 0 22px;font-family:"Montserrat",sans-serif;font-size:11px;letter-spacing:1.5px;color:var(--white);white-space:nowrap}
.btn i{width:44px;height:24px;border-radius:12px;background:var(--white);display:block;position:relative}
.btn i::after{content:"";position:absolute;right:3px;top:3px;width:18px;height:18px;border-radius:50%;background:var(--teal)}

/* intro */
.intro{left:0;top:690px;width:1200px;height:420px;background:var(--teal-pale);clip-path:polygon(0 8%,100% 0,100% 88%,0 100%)}
.intro-text{left:160px;top:780px;width:880px;text-align:center;font-size:17px;line-height:27px;color:var(--ink)}
.intro-text p+p{margin-top:18px}

/* section titles */
.sec-title{left:0;width:1200px;text-align:center;font-size:54px;line-height:64px;color:var(--ink)}

/* cards */
.grid{left:110px;top:1190px;width:980px;display:grid;grid-template-columns:repeat(4,230px);gap:14px 20px}
.card{width:230px;height:300px;background:var(--white);box-shadow:0 3px 12px rgba(0,0,0,.18);text-align:center;padding-top:20px;flex:none}
.card .img{width:170px;height:180px;margin:0 auto;background:linear-gradient(180deg,var(--photo-light),var(--photo-shade))}
.card h3{font-weight:500;font-size:19px;letter-spacing:.5px;margin-top:26px;text-transform:uppercase;white-space:nowrap}
.card .price{font-family:"Montserrat",sans-serif;font-size:10px;color:var(--muted);margin-top:6px}

/* dragonfly */
.pendant-photo{left:0;top:2272px;width:592px;height:488px;background:linear-gradient(160deg,#5a4a4e,#2c2826)}
.pendant-panel{left:592px;top:2272px;width:608px;height:488px;background:var(--teal-pale)}
.pendant-title{left:620px;top:2314px;font-size:50px;line-height:60px;color:var(--ink);white-space:nowrap}
.pendant-copy{left:620px;top:2398px;width:300px;font-size:16px;line-height:25px}
.label{font-family:"Montserrat",sans-serif;font-size:13px;letter-spacing:1px;font-weight:600}

/* crafted */
.crafted-title{left:110px;top:2800px;width:1000px;font-size:52px;line-height:62px;white-space:nowrap}
.crafted-copy{left:110px;top:2900px;width:500px;font-size:16px;line-height:25px}
.ring-photo{left:648px;top:2890px;width:440px;height:420px;border-radius:6px;background:linear-gradient(160deg,#5d626a,#1f2227)}

/* popular */
.popular{left:0;top:3380px;width:1200px;height:580px;background:var(--teal);clip-path:polygon(0 10%,100% 0,100% 100%,0 100%)}
.popular-title{top:3456px;color:var(--white)}
.carousel{left:-110px;top:3560px;display:flex;gap:20px}
.round-arrow{width:40px;height:40px;border-radius:50%;background:rgba(255,255,255,.85);display:flex;align-items:center;justify-content:center}

/* footer */
.footer-left{left:0;top:3968px;width:600px;height:408px;background:var(--white)}
.footer-right{left:600px;top:3968px;width:600px;height:408px;background:var(--black)}
.map{left:110px;top:4150px;width:190px;height:150px;background:linear-gradient(135deg,#e8ecdf,#d6e2e8);border:1px solid #ccc}
.address{left:320px;top:4180px;font-family:"Montserrat",sans-serif;font-size:12px;line-height:34px;color:var(--ink);letter-spacing:.5px}
.fcol{top:4010px;font-family:"Montserrat",sans-serif;color:var(--white)}
.fcol h4{font-size:13px;letter-spacing:1.5px;font-weight:600;margin-bottom:6px}
.fcol .rule{width:40px;height:2px;background:var(--teal);margin-bottom:12px}
.fcol li{list-style:none;font-size:10px;line-height:20px;letter-spacing:.5px;white-space:nowrap}
.badge{background:#cfcfcf}
.copyright{left:640px;top:4322px;font-family:"Montserrat",sans-serif;font-size:9px;color:#bdbdbd;letter-spacing:.5px}
</style>
</head>
<body>

<header class="site-header abs">
  <div class="brand abs"><span class="brand-dot"></span><span class="brand-name">Marwick Jewelers</span></div>
</header>
<div class="util-bar abs"><span>ABOUT US</span><span>CONTACT US</span><span>JEWELRY SERVICES AND REPAIRS</span><span>JEWELRY EDUCATION</span></div>
<nav class="main-nav abs">
  <span class="on">HOME</span><span>SHOP ONLINE</span><span>MARWICK SHOWCASE</span><span>CUSTOM DESIGN</span><span>MARWICK WATCHES</span><span>GIFT ITEMS</span><span>ENGRAVING &amp; TROPHIES</span>
</nav>
<div class="search abs">SEARCH</div>

<section class="hero abs" role="img" aria-label="Photo of a diamond engagement ring on a dark background with soft bokeh lights"></section>
<h1 class="hero-title abs script">Say It with a Stone</h1>
<p class="hero-sub abs script">and leave her speechless</p>
<div class="btn abs" style="left:522px;top:470px">CONTACT US<i></i></div>
<div class="arrow-tab abs" style="left:0;top:380px"><svg width="10" height="14"><path d="M8 1 2 7l6 6" stroke="#fff" stroke-width="2" fill="none"/></svg></div>
<div class="arrow-tab abs" style="left:1174px;top:380px"><svg width="10" height="14"><path d="M2 1l6 6-6 6" stroke="#fff" stroke-width="2" fill="none"/></svg></div>

<section class="intro abs"></section>
<div class="intro-text abs">
  <p>From "will you?" to "I do" and every momentous occasion in between, Marwick Jewelers offers a radiant array of elegant stones and settings to take her breath away. Our family-owned store here in Eastfield, MN upholds this promise we made more than 40 years ago: to provide professional expertise that helps you give a gift with a personal touch.</p>
  <p>Browse our online collection of fine jewelry and then visit us in person. Together we'll find a piece that speaks from the heart.</p>
</div>

<h2 class="sec-title abs script" style="top:1100px">Featured Items</h2>
<div class="grid abs">
  <div class="card"><div class="img" role="img" aria-label="Product photo: gold stackable ring"></div><h3>Stackable Ring</h3><p class="price">$79.00–$1,849.00</p></div>
  <div class="card"><div class="img" role="img" aria-label="Product photo: white gold negative space ring"></div><h3>Negative Space Ring</h3><p class="price">$64.00–$867.00</p></div>
  <div class="card"><div class="img" role="img" aria-label="Product photo: gold halo-style ring"></div><h3>Halo-Style Ring</h3><p class="price">$78.00–$1,849.00</p></div>
  <div class="card"><div class="img" role="img" aria-label="Product photo: rose gold anniversary band"></div><h3>Anniversary Band</h3><p class="price">$70.00–$1,849.00</p></div>
  <div class="card"><div class="img" role="img" aria-label="Product photo: rose gold solitaire ring"></div><h3>Solitaire Ring</h3><p class="price">$78.00–$1,849.00</p></div>
  <div class="card"><div class="img" role="img" aria-label="Product photo: white gold two-stone ring"></div><h3>Two-Stone Ring</h3><p class="price">$64.00–$867.00</p></div>
  <div class="card"><div class="img" role="img" aria-label="Product photo: gold accented band"></div><h3>Accented Band</h3><p class="price">$78.00–$1,849.00</p></div>
  <div class="card"><div class="img" role="img" aria-label="Product photo: white gold accented ring"></div><h3>Accented Ring</h3><p class="price">$70.00–$1,849.00</p></div>
  <div class="card"><div class="img" role="img" aria-label="Product photo: gold enamel ring with pearl"></div><h3>Enamel Ring</h3><p class="price">$78.00–$1,849.00</p></div>
  <div class="card"><div class="img" role="img" aria-label="Product photo: black and gold flower ring"></div><h3>Flower Ring</h3><p class="price">$64.00–$867.00</p></div>
  <div class="card"><div class="img" role="img" aria-label="Product photo: gold stackable V ring"></div><h3>Stackable V Ring</h3><p class="price">$78.00–$1,849.00</p></div>
  <div class="card"><div class="img" role="img" aria-label="Product photo: gold round signet ring"></div><h3>Round Signet Ring</h3><p class="price">$70.00–$1,849.00</p></div>
</div>
<div class="btn abs" style="left:518px;top:2142px">VIEW MORE<i></i></div>

<div class="pendant-photo abs" role="img" aria-label="Photo of a custom dragonfly pendant with colored gemstones on a chain"></div>
<section class="pendant-panel abs"></section>
<h2 class="pendant-title abs script">Custom Dragonfly Pendant</h2>
<div class="pendant-copy abs">
  <p>From "will you?" to "I do" and every momentous occasion in between, Marwick Jewelers offers a radiant array of elegant stones and settings to take her breath away. Our family-owned store here in Eastfield, MN upholds this promise we made more than 40 years ago to provide professional expertise that helps you give a gift with a personal touch.</p>
  <p class="label" style="margin-top:14px">PRICE RANGE</p>
  <p>Prices vary</p>
</div>
<div class="btn abs" style="left:620px;top:2672px">CONTACT US<i></i></div>

<h2 class="crafted-title abs script">Jewelry Crafted with Decades of Experience</h2>
<p class="crafted-copy abs">Marwick Jewelers is an independent, family owned jewelry store located in the heart of Downtown Eastfield. Owner, Owen Marwick has been with the business since 1990. His wife, Claire, joined the business in 2010, store manager, Dana, came on board in 2014 and Rosa joined the team in 2021. Marwick Jewelers specializes in engagement rings, fashion jewelry and custom designed pieces. Whether you want to create the ring of your dreams or to create a family heirloom, Marwick Jewelers is the place to go. Marwick Jewelers offers on-site repairs and more.</p>
<div class="btn abs" style="left:110px;top:3200px">VIEW MORE<i></i></div>
<div class="ring-photo abs" role="img" aria-label="Photo of a diamond halo engagement ring on a dark surface"></div>

<section class="popular abs"></section>
<h2 class="sec-title popular-title abs script">Most Popular</h2>
<div class="carousel abs">
  <div class="card"><div class="img" role="img" aria-label="Product photo: white gold accented ring"></div><h3>Accented Ring</h3><p class="price">$70.00–$1,849.00</p></div>
  <div class="card"><div class="img" role="img" aria-label="Product photo: rose gold solitaire ring"></div><h3>Solitaire Ring</h3><p class="price">$78.00–$1,849.00</p></div>
  <div class="card"><div class="img" role="img" aria-label="Product photo: white gold two-stone ring"></div><h3>Two-Stone Ring</h3><p class="price">$64.00–$867.00</p></div>
  <div class="card"><div class="img" role="img" aria-label="Product photo: gold accented band"></div><h3>Accented Band</h3><p class="price">$78.00–$1,849.00</p></div>
  <div class="card"><div class="img" role="img" aria-label="Product photo: white gold accented ring"></div><h3>Accented Ring</h3><p class="price">$70.00–$1,849.00</p></div>
  <div class="card"><div class="img" role="img" aria-label="Product photo: gold accented band"></div><h3>Accented Band</h3><p class="price">$78.00–$1,849.00</p></div>
</div>
<div class="round-arrow abs" style="left:34px;top:3690px"><svg width="12" height="14"><path d="M9 1 3 7l6 6" stroke="#3d7b86" stroke-width="2" fill="none"/></svg></div>
<div class="round-arrow abs" style="left:1126px;top:3690px"><svg width="12" height="14"><path d="M3 1l6 6-6 6" stroke="#3d7b86" stroke-width="2" fill="none"/></svg></div>

<footer>
  <div class="footer-left abs"></div>
  <div class="brand abs" style="top:4010px;left:110px"><span class="brand-dot"></span><span class="brand-name" style="font-size:40px">Marwick Jewelers</span></div>
  <div class="map abs" role="img" aria-label="Small street map showing the store location"></div>
  <div class="address abs">
    <div>140 HARBOR ST N, EASTFIELD, MN</div>
    <div>555-201-4470 – PHONE</div>
    <div>800-555-0148 – TOLL FREE</div>
  </div>
  <div class="footer-right abs"></div>
  <div class="fcol abs" style="left:640px">
    <h4>QUICK LINKS</h4><div class="rule"></div>
    <ul><li>SHOP ONLINE</li><li>MARWICK SHOWCASE</li><li>CUSTOM DESIGN</li><li>MARWICK WATCHES</li><li>GIFT ITEMS</li><li>ENGRAVING &amp; TROPHIES</li></ul>
  </div>
  <div class="fcol abs" style="left:820px">
    <h4>LINKS</h4><div class="rule"></div>
    <ul><li>ABOUT US</li><li>CONTACT US</li><li>JEWELRY SERVICES AND REPAIRS</li><li>JEWELRY EDUCATION</li></ul>
  </div>
  <div class="badge abs" style="left:1040px;top:4020px;width:50px;height:40px;border-radius:50%"></div>
  <div class="badge abs" style="left:1030px;top:4080px;width:90px;height:40px"></div>
  <p class="copyright abs">©2024 MARWICK JEWELERS. NORTH LAKES JEWELERS. ALL RIGHTS RESERVED.</p>
</footer>

</body>
</html>
```